Fresh, modern, fun business card for pediatric dental practice

Need a business card for fresh, modern, fun pediatric dental practice

Clean look that matches our website's font and colors

We prefer the look of curved corners on business cards

Target Market(s)

parents (mothers) of young children, professionals, mid-high class

Industry/Entity Type

Dental

Contact Information for Business Card

Maplebrook Pediatric Dentistry
482 Orchard Vale Road
Suite 517
Fernwick, PA 17028
555.419.3067
www.maplebrookkidsdental.example

Mara Tevlin, DMD
Colette Varnum, DMD
(we are working on our email address, but we would like that on the card as well)

Font styles to use
Sans Serif

Requirements
Must have
• All info; we would also like to make cards for individual staff members
• colors from our website and color palatte, attatched
• use same font and design as website for branding
Nice to have
• clean, simple card that has a pop of color
• we would like to see a few designs with our tag line "where smiles get brighter"
• we are not sure if we want to have it on there or not
• we would like to see a few designs incorporating the ribbon graphic on our website where the word WELCOME is

```html
<!DOCTYPE html>
<html lang="en">
<head>
<meta charset="utf-8">
<title>Maplebrook Pediatric Dentistry – Business Card</title>
<link rel="stylesheet" href="https://fonts.googleapis.com/css2?family=Lato:wght@400;700&display=swap">
<style>
  :root {
    --pink: #d23a9f;
    --pink-deep: #c22a8f;
    --pink-light: #e25bb8;
    --sun: #e9b437;
    --ink: #5a5a5a;
    --paper: #ffffff;
    --backdrop: #e9e7ea;
  }
  * { box-sizing: border-box; margin: 0; padding: 0; }
  html, body {
    width: 1200px; height: 900px; overflow: hidden;
    background: var(--backdrop);
    font-family: "Lato", sans-serif;
  }
  .canvas { position: relative; width: 1200px; height: 900px; }
  .card {
    position: absolute; left: 300px; width: 600px; height: 343px;
    border-radius: 22px; overflow: hidden;
    box-shadow: 0 10px 28px rgba(0,0,0,0.18);
  }
  .card-front { top: 77px; background: var(--paper); }
  .card-back { top: 480px; }

  /* front */
  .brand {
    position: absolute; left: 40px; top: 128px; width: 240px;
    display: flex; align-items: center; gap: 12px;
  }
  .brand-dot {
    flex: none; width: 28px; height: 28px; border-radius: 50%;
    background: var(--sun);
  }
  .brand-name {
    color: var(--sun); font-weight: 700; font-size: 29px; line-height: 1.05;
    letter-spacing: 0.5px;
  }
  .brand-name small { display: block; font-size: 15px; letter-spacing: 1.4px; margin-top: 4px; }
  .divider {
    position: absolute; left: 300px; top: 70px; width: 2px; height: 200px;
    background: var(--sun);
  }
  .details {
    position: absolute; left: 324px; top: 80px; right: 24px;
    color: var(--ink); font-size: 13.5px; line-height: 1.4;
  }
  .person { font-size: 23px; font-weight: 700; color: var(--pink); margin-bottom: 8px; }
  .person .title { color: var(--sun); font-weight: 400; }
  .practice { color: var(--pink); font-weight: 700; font-size: 13.5px; }
  .contact { list-style: none; margin-top: 12px; }
  .contact li { display: flex; align-items: center; gap: 8px; margin-bottom: 3px; font-size: 13px; white-space: nowrap; }
  .contact svg { flex: none; width: 17px; height: 17px; }

  /* back */
  .back-pattern {
    position: absolute; inset: 0;
    background: linear-gradient(135deg, var(--pink-light), var(--pink-deep));
  }
  .back-brand {
    position: absolute; left: 0; right: 0; top: 128px; text-align: center;
    color: #fbeaf5; font-weight: 700; font-size: 44px; line-height: 1; letter-spacing: 1px;
  }
  .back-brand small { display: block; font-size: 19px; letter-spacing: 2px; margin-top: 6px; }
</style>
</head>
<body>
<main class="canvas">
  <section class="card card-front">
    <div class="brand">
      <span class="brand-dot"></span>
      <p class="brand-name">maplebrook<small>pediatric dentistry</small></p>
    </div>
    <div class="divider"></div>
    <div class="details">
      <h1 class="person">Mara Tevlin, <span class="title">DMD</span></h1>
      <p class="practice">Maplebrook Pediatric Dentistry</p>
      <p>482 Orchard Vale Road, Suite 517<br>Fernwick, PA 17028</p>
      <ul class="contact">
        <li>
          <svg viewBox="0 0 20 20"><circle cx="10" cy="10" r="10" fill="var(--pink)"/><path d="M7 5.5l2 2-1.2 1.4a6 6 0 0 0 3.3 3.3l1.4-1.2 2 2-1.3 1.5C9.8 14.4 5.6 10.2 5.5 6.8z" fill="#fff"/></svg>
          555.419.3067
        </li>
        <li>
          <svg viewBox="0 0 20 20"><circle cx="10" cy="10" r="10" fill="var(--pink)"/><rect x="5" y="6.5" width="10" height="7" rx="1" fill="#fff"/><path d="M5.5 7l4.5 3.5L14.5 7" fill="none" stroke="var(--pink)" stroke-width="1.2"/></svg>
          info@maplebrookkidsdental.example
        </li>
        <li>
          <svg viewBox="0 0 20 20"><circle cx="10" cy="10" r="10" fill="var(--pink)"/><circle cx="10" cy="10" r="5" fill="none" stroke="#fff" stroke-width="1.3"/><path d="M5 10h10M10 5c-2.5 3-2.5 7 0 10M10 5c2.5 3 2.5 7 0 10" fill="none" stroke="#fff" stroke-width="1"/></svg>
          www.maplebrookkidsdental.example
        </li>
      </ul>
    </div>
  </section>

  <section class="card card-back">
    <div class="back-pattern" role="img" aria-label="Repeating pattern of small orange spiral suns on a magenta background"></div>
    <p class="back-brand">maplebrook<small>pediatric dentistry</small></p>
  </section>
</main>
</body>
</html>
```